Flyer-Design für Kindertagesstätte
Helmsteds Kinderhafen suchte ein neues Design in der Kategorie Flyer und hat ein Projekt auf grafikfinden.de gestartet.
Zielgruppe
Wir sind eine Kindertagesstätte und wollen eine Baby-Kind-Spielgruppe jeden Mittwoch in unserer Kita von 09.00 Uhr bis 11.00 Uhr anbieten.
Aufgabenstellung
Unser LOGO muss im Flyer enthalten sein, auf jeden Fall ein Bild wenn möglich mit mehreren Babys/Kleinkindern bis 1,5 Jahre. Wir benötigen den Flyer in DIN lang - bunt - 1 seitig.
Folgender Text sollte enthalten: Baby-Kind-Spielgruppe, jeden mittwoch in unserer Kita 'Helmsteds Kinderhafen' von 09.00 Uhr bis 11.00 Uhr. Die Spielgruppe wird durch unser ausgebildetes Fachpersonal begleitet.

```html
<!DOCTYPE html>
<html lang="de">
<head>
<meta charset="utf-8">
<title>Baby-Kind Spielgruppe – Flyer</title>
<link rel="stylesheet" href="https://fonts.googleapis.com/css2?family=Arvo:wght@700&family=Montserrat+Alternates:wght@400;500&display=swap">
<style>
  :root{
    --orange:#f26522;
    --orange-deep:#e8561f;
    --white:#ffffff;
    --page:#f4f2ef;
    --green:#8dbb34;
    --blue:#1ab0e0;
    --mustard:#d9a21b;
    --pink:#e4449b;
    --brand:#5a1e12;
  }
  *{box-sizing:border-box;margin:0;padding:0}
  html,body{width:800px;height:1200px;overflow:hidden;background:var(--page)}
  .flyer{
    position:absolute;left:134px;top:28px;width:532px;height:1143px;
    background:var(--orange);overflow:hidden;
    font-family:"Montserrat Alternates",sans-serif;
    box-shadow:0 6px 24px rgba(0,0,0,.12);
  }
  .photo-kids{
    position:absolute;left:0;top:100px;width:532px;height:480px;
    background:linear-gradient(100deg,#c9b8a0 0%,#e8c9a8 30%,#f2d25a 48%,#e9b7b2 68%,#f0c9c4 100%);
  }
  .clouds{position:absolute;left:0;top:0;width:532px;height:1143px}
  .logo{
    position:absolute;left:130px;top:170px;width:200px;text-align:center;
    color:var(--brand);font-weight:500;font-size:22px;line-height:1.15;
  }
  .block{
    position:absolute;width:104px;height:104px;border-radius:14px;
    display:flex;align-items:center;justify-content:center;
    font-family:"Arvo",serif;font-weight:700;font-size:78px;color:var(--white);
    box-shadow:inset 0 0 0 6px rgba(0,0,0,.08);
  }
  .block--orange{background:var(--orange-deep)}
  .block--green{background:var(--green)}
  .block--blue{background:var(--blue)}
  .block--mustard{background:var(--mustard)}
  .block--pink{background:var(--pink)}
  .title-dash{position:absolute;left:212px;top:624px;width:40px;height:9px;background:var(--mustard)}
  .subtitle{
    position:absolute;left:0;width:532px;top:764px;text-align:center;
    color:var(--orange);font-weight:500;font-size:38px;
  }
  .photo-baby{
    position:absolute;left:307px;top:802px;width:225px;height:341px;
    border-radius:110px 110px 0 60px;
    background:linear-gradient(180deg,#f3d3c6 0%,#efc1b4 30%,#b53fa8 55%,#9c2f96 100%);
  }
  .info{position:absolute;left:44px;top:880px;width:280px;list-style:none}
  .info__item{display:flex;align-items:flex-start;color:var(--white);font-size:19px;line-height:1.15;margin-bottom:24px}
  .info__item svg{flex:0 0 46px;width:46px;height:46px;margin-right:20px}
</style>
</head>
<body>
<div class="flyer">
  <div class="photo-kids" role="img" aria-label="Foto: zwei Kleinkinder spielen mit buntem Holzspielzeug"></div>

  <svg class="clouds" viewBox="0 0 532 1143" aria-hidden="true">
    <g fill="#ffffff">
      <circle cx="265" cy="105" r="105"/>
      <circle cx="160" cy="190" r="72"/>
      <circle cx="370" cy="190" r="72"/>
      <rect x="160" y="120" width="210" height="140" rx="60"/>
    </g>
    <g fill="#ffffff">
      <ellipse cx="266" cy="670" rx="300" ry="140"/>
      <circle cx="260" cy="580" r="118"/>
      <circle cx="280" cy="770" r="95"/>
      <circle cx="100" cy="715" r="92"/>
      <circle cx="445" cy="720" r="85"/>
    </g>
  </svg>

  <div class="logo">Helmsteds<br>Kinderhafen</div>

  <div class="block block--orange" style="left:43px;top:505px;transform:rotate(-4deg)">B</div>
  <div class="block block--green" style="left:166px;top:500px;transform:rotate(-2deg)">A</div>
  <div class="block block--blue" style="left:280px;top:497px;transform:rotate(3deg)">B</div>
  <div class="block block--mustard" style="left:402px;top:490px;transform:rotate(-3deg)">Y</div>

  <div class="title-dash"></div>

  <div class="block block--mustard" style="left:35px;top:642px;transform:rotate(-5deg)">K</div>
  <div class="block block--pink" style="left:151px;top:645px;transform:rotate(2deg)">I</div>
  <div class="block block--orange" style="left:268px;top:632px;transform:rotate(-6deg)">N</div>
  <div class="block block--green" style="left:384px;top:622px;transform:rotate(3deg)">D</div>

  <div class="subtitle">Spielgruppe</div>

  <div class="photo-baby" role="img" aria-label="Foto: Baby im pinken Kleid spielt mit einem Stapelbecher"></div>

  <ul class="info">
    <li class="info__item">
      <svg viewBox="0 0 46 46" fill="none" stroke="#fff" stroke-width="3"><rect x="5" y="8" width="36" height="34" rx="6"/><line x1="15" y1="3" x2="15" y2="12"/><line x1="31" y1="3" x2="31" y2="12"/><text x="23" y="35" fill="#fff" stroke="none" font-family="Arvo,serif" font-weight="700" font-size="15" text-anchor="middle">11</text></svg>
      <span>jeden Mittwoch<br>in unserer Kita</span>
    </li>
    <li class="info__item">
      <svg viewBox="0 0 46 46" fill="none" stroke="#fff" stroke-width="3.5" stroke-linejoin="round"><path d="M23 40 C10 30 4 23 4 15 C4 9 9 5 14 5 C18 5 21 8 23 11 C25 8 28 5 32 5 C37 5 42 9 42 15 C42 23 36 30 23 40 Z"/></svg>
      <span>durch unser ausge-<br>bildetes Fachperso-<br>nal begleitet</span>
    </li>
    <li class="info__item">
      <svg viewBox="0 0 46 46" fill="none" stroke="#fff" stroke-width="3" stroke-linecap="round"><circle cx="23" cy="23" r="19"/><line x1="23" y1="23" x2="23" y2="12"/><line x1="23" y1="23" x2="31" y2="29"/></svg>
      <span>von 09.00 Uhr bis<br>11.00 Uhr</span>
    </li>
  </ul>
</div>
</body>
</html>
```